Finiding oppertunites in Real Estate 6.15.20

size of ad 7” x 9.6”
1-I like the ad to stand out and attract people's attention.
2-you should be able to see the text of the ad clearly .. see the attachment anything in yellow is instructions.
3-the list of topics should not be the main part of the ad
4-if you decide you want a picture or vector of a person .. (you decide)
then it should be a white male about 25-30 years old wearing a solid white or blue shirt and not long hair.
5-leave 1 inch for footer
see attachment
Good luck

Target Market(s)

potential male students 25-35 years of age

Industry/Entity Type

Education

Requirements
Must have
• will stand out and people would want to see it.
should be able to read the words of ad
Nice to have
• how to make money in real estate on one line

```html
<!DOCTYPE html>
<html lang="en">
<head>
<meta charset="utf-8">
<title>Real Estate Career Course</title>
<link rel="stylesheet" href="https://fonts.googleapis.com/css2?family=Anton&family=Montserrat:wght@300;400;700;800&display=swap">
<style>
  :root {
    --charcoal: #302f34;
    --charcoal-soft: #4a494f;
    --yellow: #ffcc00;
    --yellow-deep: #f5b800;
    --white: #ffffff;
    --ink: #2f2e33;
    --muted: #46454a;
    --stage: #d9d9d9;
  }
  * { margin: 0; padding: 0; box-sizing: border-box; }
  html, body { width: 1200px; height: 1200px; overflow: hidden; background: var(--stage); }
  .flyer {
    position: absolute; left: 162px; top: 0;
    width: 875px; height: 1200px;
    background: var(--white);
    overflow: hidden;
    font-family: "Montserrat", Arial, sans-serif;
    color: var(--ink);
  }
  .hero { position: absolute; left: 0; top: 0; width: 875px; height: 580px; }
  .hero svg { position: absolute; left: 0; top: 0; }
  .title {
    position: absolute; left: 60px;
    font-family: "Anton", "Oswald", sans-serif;
    line-height: 1; white-space: nowrap; text-transform: uppercase;
  }
  .title-real   { top: 200px; font-size: 128px; color: var(--white); }
  .title-estate { top: 325px; font-size: 128px; color: var(--white); }
  .title-course { top: 453px; font-size: 71px; color: var(--yellow); }

  .headline {
    position: absolute; left: 60px; top: 610px;
    font-weight: 800; font-size: 52px; line-height: 51px;
    text-transform: uppercase; white-space: nowrap; color: var(--ink);
  }
  .benefits { position: absolute; left: 60px; top: 737px; list-style: none; }
  .benefits li {
    display: flex; align-items: center; gap: 9px;
    font-size: 19.5px; font-weight: 400; color: var(--muted);
    height: 28px; white-space: nowrap; letter-spacing: 0.2px;
  }
  .tick { flex: none; }

  .schedule {
    position: absolute; left: 0; top: 833px; width: 875px; height: 158px;
    background: linear-gradient(90deg, #5a595e 0%, var(--charcoal) 22%, var(--charcoal) 100%);
  }
  .schedule-text {
    position: absolute; left: 60px; top: 20px;
    color: var(--white); font-weight: 700; font-size: 50px; line-height: 57px; white-space: nowrap;
  }
  .burst { position: absolute; left: 538px; top: 780px; width: 280px; height: 280px; }
  .burst-label {
    position: absolute; left: 538px; top: 780px; width: 280px; height: 280px;
    display: flex; align-items: center; justify-content: center; text-align: center;
    font-weight: 800; font-size: 27px; line-height: 30px; color: var(--ink);
  }

  .topics-title {
    position: absolute; left: 60px; top: 1010px;
    font-weight: 700; font-size: 29px; color: var(--ink); white-space: nowrap;
  }
  .topics { position: absolute; top: 1064px; list-style: none; }
  .topics li {
    display: flex; align-items: center; gap: 6px;
    font-size: 16.5px; font-weight: 400; color: var(--muted);
    height: 22.6px; white-space: nowrap; letter-spacing: 0.3px;
  }
  .col-1 { left: 60px; }
  .col-2 { left: 277px; }
  .col-3 { left: 497px; }
  .col-4 { left: 665px; }
</style>
</head>
<body>
<svg width="0" height="0" style="position:absolute">
  <defs>
    <symbol id="tick-icon" viewBox="0 0 20 20">
      <circle cx="10" cy="10" r="8.2" fill="none" stroke="currentColor" stroke-width="1.8"/>
      <path d="M6.2 10.3 L8.9 13 L13.9 7.4" fill="none" stroke="currentColor" stroke-width="1.9" stroke-linecap="round" stroke-linejoin="round"/>
    </symbol>
  </defs>
</svg>

<main class="flyer">
  <section class="hero">
    <svg width="875" height="580" viewBox="0 0 875 580">
      <defs>
        <linearGradient id="panel-shade" x1="0" y1="0" x2="1" y2="0">
          <stop offset="0" stop-color="#55545a"/>
          <stop offset="0.3" stop-color="#302f34"/>
          <stop offset="1" stop-color="#302f34"/>
        </linearGradient>
        <linearGradient id="photo-tone" x1="0" y1="0" x2="1" y2="1">
          <stop offset="0" stop-color="#e6e6e6"/>
          <stop offset="0.45" stop-color="#6c6c6c"/>
          <stop offset="1" stop-color="#8fb6d8"/>
        </linearGradient>
      </defs>
      <polygon points="0,0 190,0 625,580 0,580" fill="url(#panel-shade)"/>
      <polygon points="190,0 254,0 642,580 625,580" fill="var(--yellow)"/>
      <polygon points="254,0 272,0 656,580 642,580" fill="var(--white)"/>
      <polygon points="272,0 875,0 875,580 656,580" fill="url(#photo-tone)" role="img" aria-label="Photo of a young man in glasses and a light blue shirt pointing at the title, in front of a black and white city skyline"/>
    </svg>
    <div class="title title-real">Real</div>
    <div class="title title-estate">Estate</div>
    <div class="title title-course">Career Course</div>
  </section>

  <h1 class="headline">How to make money<br>in in real estate?</h1>

  <ul class="benefits">
    <li><svg class="tick" width="16" height="16"><use href="#tick-icon"/></svg>For those who have started or would like to go into Real Estate</li>
    <li><svg class="tick" width="16" height="16"><use href="#tick-icon"/></svg>An investment in knowledge opens up untold opportunities</li>
  </ul>

  <section class="schedule">
    <p class="schedule-text">12 sessions<br>Starting June 16</p>
  </section>

  <svg class="burst" viewBox="0 0 280 280">
    <defs>
      <radialGradient id="burst-fill" cx="0.5" cy="0.45" r="0.6">
        <stop offset="0" stop-color="#ffe34d"/>
        <stop offset="0.7" stop-color="#ffcc00"/>
        <stop offset="1" stop-color="#f2b000"/>
      </radialGradient>
    </defs>
    <polygon transform="translate(4,5)" fill="#7a3a10" opacity="0.8" points="270,140 236.6,165.9 252.6,205 210.7,210.7 205,252.6 165.9,236.6 140,270 114.1,236.6 75,252.6 69.3,210.7 27.4,205 43.4,165.9 10,140 43.4,114.1 27.4,75 69.3,69.3 75,27.4 114.1,43.4 140,10 165.9,43.4 205,27.4 210.7,69.3 252.6,75 236.6,114.1"/>
    <polygon fill="url(#burst-fill)" points="270,140 236.6,165.9 252.6,205 210.7,210.7 205,252.6 165.9,236.6 140,270 114.1,236.6 75,252.6 69.3,210.7 27.4,205 43.4,165.9 10,140 43.4,114.1 27.4,75 69.3,69.3 75,27.4 114.1,43.4 140,10 165.9,43.4 205,27.4 210.7,69.3 252.6,75 236.6,114.1"/>
  </svg>
  <div class="burst-label">Remote<br>sessions</div>

  <h2 class="topics-title">A partial listing of Topics</h2>

  <ul class="topics col-1">
    <li><svg class="tick" width="12" height="12"><use href="#tick-icon"/></svg>Single-family</li>
    <li><svg class="tick" width="12" height="12"><use href="#tick-icon"/></svg>Multifamily</li>
    <li><svg class="tick" width="12" height="12"><use href="#tick-icon"/></svg>Management</li>
    <li><svg class="tick" width="12" height="12"><use href="#tick-icon"/></svg>Real Estate Concepts</li>
  </ul>
  <ul class="topics col-2">
    <li><svg class="tick" width="12" height="12"><use href="#tick-icon"/></svg>Real Estate law</li>
    <li><svg class="tick" width="12" height="12"><use href="#tick-icon"/></svg>Investment properties</li>
    <li><svg class="tick" width="12" height="12"><use href="#tick-icon"/></svg>Foreclosures</li>
    <li><svg class="tick" width="12" height="12"><use href="#tick-icon"/></svg>Rehab</li>
  </ul>
  <ul class="topics col-3">
    <li><svg class="tick" width="12" height="12"><use href="#tick-icon"/></svg>Foreclosures</li>
    <li><svg class="tick" width="12" height="12"><use href="#tick-icon"/></svg>Short sales</li>
    <li><svg class="tick" width="12" height="12"><use href="#tick-icon"/></svg>Development</li>
    <li><svg class="tick" width="12" height="12"><use href="#tick-icon"/></svg>Finical modeling</li>
  </ul>
  <ul class="topics col-4">
    <li><svg class="tick" width="12" height="12"><use href="#tick-icon"/></svg>HUD properties</li>
    <li><svg class="tick" width="12" height="12"><use href="#tick-icon"/></svg>Due Diligence e</li>
  </ul>
</main>
</body>
</html>
```